Charity Initiative needs a WebPage design

We need a web design for charity initiative by two young guys riding their bikes around Australia to support Kestrelwood which helps people with depression and anxiety. Full brief and requirements are attached in the PDF and word document. We have the logo already done and attached. Website will be done in Wordpress and need to get Donations, display current donations, show live Video feed, GPS tracker, Blogs etc and also ability to sell merchandise later

Target Market(s)

Sponsors, Business, Young People

Number of Pages Required

4 page

Font styles to use
Serif
Sans Serif
Decorative
Script

Requirements
Must have
• As per Brief and also Donation status etc
Nice to have
• Please check my logo and read the Bried

```html
<!DOCTYPE html>
<html lang="en">
<head>
<meta charset="utf-8">
<title>Coastline Throttle — The Motorcycle Adventure Around Australia</title>
<link rel="stylesheet" href="https://fonts.googleapis.com/css2?family=Roboto:wght@400;500;700&family=Roboto+Condensed:wght@700&family=Rubik+Dirt&display=swap">
<style>
  :root {
    --pink: #e8336f;
    --pink-deep: #c92658;
    --teal: #3bb3a6;
    --black: #0d0d0d;
    --white: #ffffff;
    --ink: #2b2b2b;
    --muted: #555555;
    --sea: #2a6db3;
    --moss: #3f6b3a;
  }
  * { box-sizing: border-box; margin: 0; padding: 0; }
  html, body { width: 1200px; height: 2525px; overflow: hidden; }
  body { font-family: "Roboto", Arial, sans-serif; color: var(--ink); position: relative; }

  .backdrop {
    position: absolute; inset: 0;
    background: linear-gradient(90deg, var(--moss) 0%, #5e7f8c 12%, var(--sea) 88%, #3a80c4 100%);
  }
  .page {
    position: absolute; left: 161px; top: 0; width: 878px; height: 2525px;
    background: var(--white);
  }
  .block { position: absolute; left: 0; width: 878px; }
  .abs { position: absolute; }

  .btn {
    position: absolute; display: flex; align-items: center; justify-content: center;
    font-family: "Roboto", Arial, sans-serif; color: var(--white); text-decoration: none;
  }
  .btn--pink { background: var(--pink); }
  .btn--teal { background: var(--teal); }
  .btn--black { background: var(--black); font-weight: 700; font-size: 13px; }

  /* header */
  .site-header { top: 0; height: 182px; }
  .brand { left: 22px; top: 40px; display: flex; align-items: center; gap: 14px; }
  .brand__dot { width: 70px; height: 70px; border-radius: 50%; background: var(--pink); }
  .brand__name { font-family: "Roboto Condensed", Arial, sans-serif; font-size: 40px; color: var(--teal); line-height: 1; width: 200px; }
  .btn--header { left: 651px; top: 67px; width: 180px; height: 50px; font-family: "Rubik Dirt", Impact, sans-serif; font-size: 22px; }

  /* nav */
  .main-nav { top: 182px; height: 42px; background: var(--black); }
  .main-nav__links { left: 30px; top: 0; height: 42px; display: flex; align-items: center; }
  .main-nav__link { color: var(--white); font-size: 17px; font-weight: 500; margin-right: 34px; position: relative; }
  .main-nav__link--active::before {
    content: ""; position: absolute; left: -8px; right: -12px; top: 4px; bottom: 2px;
    background: var(--teal); z-index: -1; transform: skewX(-20deg);
  }
  .main-nav__link--active { z-index: 1; }
  .social { right: 24px; top: 8px; display: flex; gap: 8px; }
  .social__item { height: 27px; padding: 0 5px; border: 1px solid var(--white); color: var(--white); font-size: 10px; display: flex; align-items: center; }

  /* hero */
  .hero { top: 224px; height: 449px; background: var(--pink); }
  .hero__video { left: 29px; top: 37px; width: 382px; height: 252px; background: linear-gradient(160deg, #3e6a3a, #6c8f50 55%, #8b8b8b); border: 4px solid var(--black); }
  .hero__play { left: 171px; top: 105px; }
  .hero__title { left: 435px; top: 28px; width: 420px; font-family: "Rubik Dirt", Impact, sans-serif; font-size: 30px; line-height: 1.1; color: var(--white); }
  .stats { left: 427px; top: 138px; width: 429px; height: 135px; background: var(--black); display: flex; align-items: center; }
  .stats__item { flex: 1; text-align: center; border-left: 1px solid #444; }
  .stats__item:first-child { border-left: 0; }
  .stats__label { color: var(--white); font-size: 21px; }
  .stats__value { color: var(--pink); font-size: 27px; font-weight: 700; margin-top: 12px; font-family: "Roboto Condensed", Arial, sans-serif; }
  .hero__tagline { left: 0; width: 878px; top: 310px; text-align: center; font-family: "Rubik Dirt", Impact, sans-serif; font-size: 28px; color: var(--white); }
  .hero__sub { left: 0; width: 878px; top: 348px; text-align: center; font-size: 27px; color: var(--black); }
  .btn--hero { left: 360px; top: 388px; width: 173px; height: 42px; font-size: 21px; }

  .section-title { left: 0; width: 878px; text-align: center; font-family: "Roboto Condensed", Arial, sans-serif; font-size: 40px; }
  .section-title__accent { color: var(--pink); }
  .section-rule { left: 397px; width: 84px; height: 3px; background: var(--black); }

  /* location */
  .location { top: 673px; height: 105px; }
  .location .section-title { top: 16px; color: var(--teal); }
  .location .section-rule { top: 76px; }
  .map { top: 778px; height: 346px; background: linear-gradient(135deg, #ece8e1, #e1ddd4); }

  /* fund */
  .fund { top: 1124px; height: 446px; background: linear-gradient(180deg, #6fc0bb 0%, #a9dcd6 40%, #5d6b6c 70%, #2e2e2e 100%); }
  .fund .section-title { top: 38px; color: var(--black); }
  .fund .section-rule { top: 100px; }
  .fund__flag { text-align: center; font-size: 12px; font-weight: 700; color: var(--black); }
  .fund__tag { display: inline-block; background: var(--black); color: var(--pink); font-weight: 700; padding: 6px 8px; margin-top: 4px; }
  .fund__tag--big { font-size: 20px; padding: 10px 16px; color: var(--white); }
  .fund__bar { left: 50px; top: 216px; width: 776px; height: 54px; background: var(--black); }
  .btn--fund { left: 352px; top: 305px; width: 177px; height: 54px; font-size: 21px; }

  /* journals */
  .journals { top: 1570px; height: 424px; background: linear-gradient(180deg, var(--pink-deep), #d63a66); }
  .journals .section-title { top: 22px; color: var(--white); }
  .journals .section-rule { top: 86px; }
  .journal-card { top: 118px; width: 342px; }
  .journal-card__image { width: 342px; height: 124px; background: linear-gradient(160deg, #6b6b6b, #9aa09a 60%, #3f4a3c); border: 2px solid #ddd; position: relative; }
  .journal-card__date { position: absolute; left: 0; top: 0; width: 36px; height: 46px; background: var(--black); color: var(--white); text-align: center; font-size: 8px; font-weight: 700; padding-top: 2px; }
  .journal-card__date b { display: block; font-size: 20px; line-height: 1; }
  .journal-card__comments { text-align: right; color: var(--white); font-size: 10px; margin-top: 6px; }
  .journal-card__title { color: var(--white); font-weight: 700; font-size: 14px; margin-top: 2px; padding-left: 4px; }
  .journal-card__text { color: var(--white); font-size: 13px; line-height: 1.4; padding-left: 4px; margin-top: 4px; }
  .journal-card .btn--black { position: relative; width: 100px; height: 28px; margin: 10px 0 0 5px; }

  /* riders */
  .riders { top: 1994px; height: 396px; }
  .rider { top: 56px; width: 260px; text-align: center; }
  .rider__photo { width: 135px; height: 135px; border-radius: 50%; background: linear-gradient(160deg, #a88d6b, #6c5740); margin: 0 auto; }
  .rider__photo--partner { background: #eeeeee; display: flex; align-items: center; justify-content: center; font-size: 13px; color: var(--sea); }
  .rider__name { font-size: 24px; font-weight: 500; margin-top: 20px; color: var(--ink); }
  .rider__text { width: 215px; margin: 8px auto 0; font-size: 12.5px; line-height: 1.45; color: var(--muted); }
  .rider .btn--black { position: relative; width: 100px; height: 28px; margin: 18px auto 0; }

  /* newsletter */
  .newsletter { top: 2390px; height: 91px; background: var(--teal); }
  .newsletter__label { left: 66px; top: 36px; color: var(--white); font-size: 14px; }
  .newsletter__field { left: 331px; top: 30px; width: 297px; height: 33px; border: 1px solid var(--white); color: var(--white); font-size: 12px; padding: 9px 12px; }
  .newsletter__submit { left: 640px; top: 30px; width: 104px; height: 33px; border: 1px solid var(--white); color: var(--white); font-size: 12px; font-weight: 700; display: flex; align-items: center; justify-content: center; }

  /* footer */
  .site-footer { top: 2481px; height: 44px; background: var(--black); color: var(--white); }
  .site-footer__copy { left: 22px; top: 14px; font-size: 12px; font-weight: 700; }
  .payments { right: 14px; top: 9px; display: flex; align-items: center; gap: 6px; font-size: 12px; font-weight: 700; }
  .payments__card { height: 26px; padding: 0 5px; background: var(--white); color: var(--black); font-size: 10px; display: flex; align-items: center; border-radius: 2px; }
</style>
</head>
<body>
  <div class="backdrop" role="img" aria-label="Photograph of a rocky coastline with blue sea and trees"></div>

  <main class="page">
    <header class="block site-header">
      <div class="abs brand">
        <span class="brand__dot"></span>
        <span class="brand__name">Coastline Throttle</span>
      </div>
      <a class="btn btn--pink btn--header">Donate Now</a>
    </header>

    <nav class="block main-nav">
      <div class="abs main-nav__links">
        <a class="main-nav__link main-nav__link--active">Home</a>
        <a class="main-nav__link">Journal</a>
        <a class="main-nav__link">Riders</a>
        <a class="main-nav__link">Riders</a>
        <a class="main-nav__link">Contact Us</a>
      </div>
      <div class="abs social">
        <span class="social__item">Loop</span>
        <span class="social__item">Chirp</span>
        <span class="social__item">Orbit</span>
        <span class="social__item">Mesh</span>
        <span class="social__item">Glint</span>
      </div>
    </nav>

    <section class="block hero">
      <div class="abs hero__video" role="img" aria-label="Live video feed still of two motorcycle riders leaning into a bend"></div>
      <svg class="abs hero__play" width="100" height="100" viewBox="0 0 100 100" aria-hidden="true">
        <circle cx="50" cy="50" r="44" fill="none" stroke="#e8336f" stroke-width="7"/>
        <circle cx="50" cy="50" r="36" fill="#c92658"/>
        <path d="M40 32 L68 50 L40 68 Z" fill="#ffffff"/>
      </svg>
      <h1 class="abs hero__title">The Motorcycle Adventure Around Australia</h1>
      <div class="abs stats">
        <div class="stats__item"><div class="stats__label">Days</div><div class="stats__value">50</div></div>
        <div class="stats__item"><div class="stats__label">Kilometers</div><div class="stats__value">10,568</div></div>
        <div class="stats__item"><div class="stats__label">Provinces</div><div class="stats__value">33</div></div>
      </div>
      <p class="abs hero__tagline">We Helps People With Depression And Anxiety</p>
      <p class="abs hero__sub">Donate to our partner charity</p>
      <a class="btn btn--teal btn--hero">Donate Now</a>
    </section>

    <section class="block location">
      <h2 class="abs section-title">Current <span class="section-title__accent">Location</span></h2>
      <div class="abs section-rule"></div>
    </section>
    <div class="block map" role="img" aria-label="Street map with GPS tracker markers showing the riders' current location"></div>

    <section class="block fund">
      <div class="abs" style="left:0;top:0;width:878px;height:446px" role="img" aria-label="Illustration of mountains, clouds and an open road"></div>
      <h2 class="abs section-title">Fund <span class="section-title__accent">Raised</span></h2>
      <div class="abs section-rule"></div>
      <div class="abs fund__flag" style="left:18px;top:150px">We Started<br><span class="fund__tag">00 $</span></div>
      <div class="abs fund__flag" style="left:184px;top:118px">Collected<br><span class="fund__tag fund__tag--big">10,588 $</span></div>
      <div class="abs fund__flag" style="left:775px;top:150px">Target<br><span class="fund__tag">55,000 $</span></div>
      <svg class="abs fund__bar" width="776" height="54" viewBox="0 0 776 54" aria-label="Progress towards target">
        <rect width="776" height="54" fill="#0d0d0d"/>
        <g fill="#ffffff">
          <rect x="14" y="24" width="22" height="5"/><rect x="80" y="24" width="22" height="5"/>
          <rect x="278" y="24" width="22" height="5"/><rect x="344" y="24" width="22" height="5"/>
          <rect x="410" y="24" width="22" height="5"/><rect x="476" y="24" width="22" height="5"/>
          <rect x="542" y="24" width="22" height="5"/><rect x="608" y="24" width="22" height="5"/>
          <rect x="674" y="24" width="22" height="5"/><rect x="740" y="24" width="22" height="5"/>
        </g>
        <circle cx="185" cy="27" r="16" fill="#e8336f"/>
        <circle cx="185" cy="27" r="7" fill="#f3d21a"/>
      </svg>
      <a class="btn btn--pink btn--fund">Donate Now</a>
    </section>

    <section class="block journals">
      <h2 class="abs section-title">Recent Journals</h2>
      <div class="abs section-rule"></div>
      <article class="abs journal-card" style="left:59px">
        <div class="journal-card__image" role="img" aria-label="Photo of a group of motorcyclists riding on a highway">
          <div class="journal-card__date"><b>25</b>MAY<br>2016</div>
        </div>
        <div class="journal-card__comments">&#9633; 1,256</div>
        <h3 class="journal-card__title">Lorem Ipsum is simply dummy tex</h3>
        <p class="journal-card__text">When an unknown printer took a galley of type and scrambled it to make a type specimen book.</p>
        <a class="btn btn--black">Read More</a>
      </article>
      <article class="abs journal-card" style="left:486px">
        <div class="journal-card__image" role="img" aria-label="Photo of riders on red motorcycles lined up on a road">
          <div class="journal-card__date"><b>25</b>MAY<br>2016</div>
        </div>
        <div class="journal-card__comments">&#9633; 1,256</div>
        <h3 class="journal-card__title">Lorem Ipsum is simply dummy tex</h3>
        <p class="journal-card__text">When an unknown printer took a galley of type and scrambled it to make a type specimen book.</p>
        <a class="btn btn--black">Read More</a>
      </article>
    </section>

    <section class="block riders">
      <div class="abs rider" style="left:15px">
        <div class="rider__photo" role="img" aria-label="Portrait photo of rider Rowan Ellery"></div>
        <h3 class="rider__name">Rowan Ellery</h3>
        <p class="rider__text">Donec sed odio dui. Etiam porta sem malesuada magna mollis euismod. Nullam id dolor id nibh ultricies.</p>
        <a class="btn btn--black">Read More</a>
      </div>
      <div class="abs rider" style="left:306px">
        <div class="rider__photo" role="img" aria-label="Portrait photo of rider Marcus Telford"></div>
        <h3 class="rider__name">Marcus Telford</h3>
        <p class="rider__text">Donec sed odio dui. Etiam porta sem malesuada magna mollis euismod. Nullam id dolor id nibh ultricies.</p>
        <a class="btn btn--black">Read More</a>
      </div>
      <div class="abs rider" style="left:597px">
        <div class="rider__photo rider__photo--partner">Kestrelwood</div>
        <h3 class="rider__name">Kestrelwood</h3>
        <p class="rider__text">Donec sed odio dui. Etiam porta sem malesuada magna mollis euismod. Nullam id dolor id nibh ultricies.</p>
        <a class="btn btn--black">Visit</a>
      </div>
    </section>

    <section class="block newsletter">
      <p class="abs newsletter__label">Stay updated with latest news from</p>
      <div class="abs newsletter__field">Enter Your Email</div>
      <div class="abs newsletter__submit">Subscribe</div>
    </section>

    <footer class="block site-footer">
      <p class="abs site-footer__copy">Copyright © 2016 Coastline Throttle . All Rights Reserved.</p>
      <div class="abs payments">
        <span>We Accept :</span>
        <span class="payments__card">Walletry</span>
        <span class="payments__card">Carda</span>
        <span class="payments__card">Duocard</span>
        <span class="payments__card">Farpay</span>
      </div>
    </footer>
  </main>
</body>
</html>
```